Designs for a Barrister's chambers

Design stationery (including business card and letterhead) for a barrister's chambers -- similar to a law firm, using the enclosed logo. The current designs are not fit for purpose.

```html
<!DOCTYPE html>
<html lang="en">
<head>
<meta charset="utf-8">
<title>Ledgerwood Chambers – Business Card</title>
<link href="https://fonts.googleapis.com/css2?family=Montserrat:wght@600;700&family=Open+Sans:wght@400&display=swap" rel="stylesheet">
<style>
  :root {
    --navy: #0b1f3d;
    --navy-deep: #071830;
    --navy-soft: #0f2747;
    --teal: #0096b5;
    --white: #ffffff;
    --ink: #1a1f2a;
    --rule: #e3e6ea;
    --stage: #2a2a2a;
  }
  * { margin: 0; padding: 0; box-sizing: border-box; }
  html, body { width: 1200px; height: 1015px; overflow: hidden; }
  body {
    background: var(--stage);
    font-family: "Open Sans", Arial, sans-serif;
    position: relative;
  }
  .card {
    position: absolute;
    left: 320px;
    width: 560px;
    height: 320px;
    overflow: hidden;
    box-shadow: 0 14px 30px rgba(0,0,0,0.55);
  }
  .card-back {
    top: 130px;
    background: linear-gradient(135deg, var(--navy-soft), var(--navy-deep));
    display: flex;
    align-items: center;
    justify-content: center;
  }
  .card-front { top: 540px; background: var(--white); }

  .wordmark {
    display: flex;
    align-items: center;
    gap: 18px;
    font-family: "Montserrat", Arial, sans-serif;
    font-weight: 700;
    line-height: 0.95;
    letter-spacing: -0.5px;
  }
  .wordmark-square { width: 54px; height: 54px; background: var(--teal); flex: none; }
  .wordmark-name { font-size: 40px; }
  .card-back .wordmark-name { color: var(--white); }
  .card-front .wordmark { position: absolute; left: 190px; top: 48px; }
  .card-front .wordmark-name { color: var(--navy); }

  .divider {
    position: absolute; left: 150px; right: 40px; top: 160px;
    height: 1px; background: var(--rule);
  }
  .person { position: absolute; left: 40px; top: 178px; }
  .person-name {
    font-family: "Montserrat", Arial, sans-serif;
    font-weight: 700; font-size: 22px; color: var(--teal);
  }
  .person-role { font-size: 13px; color: var(--ink); margin-top: 2px; }
  .contact-list { list-style: none; margin-top: 8px; }
  .contact-list li {
    display: flex; align-items: center; gap: 8px;
    font-size: 12.5px; color: var(--ink); line-height: 18px;
  }
  .contact-list svg { width: 12px; height: 12px; fill: var(--teal); flex: none; }

  .address {
    position: absolute; right: 34px; top: 196px;
    text-align: right; font-size: 13px; line-height: 17px; color: var(--ink);
  }
  .band-teal {
    position: absolute; left: 0; bottom: 0; width: 370px; height: 12px;
    background: var(--teal);
  }
  .band-navy {
    position: absolute; right: 0; bottom: 0; width: 200px; height: 46px;
    background: var(--navy-deep);
    display: flex; align-items: center; justify-content: center;
    font-size: 11.5px; color: var(--teal);
  }
</style>
</head>
<body>
  <section class="card card-back">
    <div class="wordmark">
      <span class="wordmark-square"></span>
      <span class="wordmark-name">Ledgerwood<br>Chambers</span>
    </div>
  </section>

  <section class="card card-front">
    <div class="wordmark">
      <span class="wordmark-square"></span>
      <span class="wordmark-name">Ledgerwood<br>Chambers</span>
    </div>
    <div class="divider"></div>

    <div class="person">
      <p class="person-name">Marcus Hallowell</p>
      <p class="person-role">Barrister</p>
      <ul class="contact-list">
        <li><svg viewBox="0 0 12 12"><path d="M2.5 1l2 2.2-1 1.3c.7 1.5 1.8 2.6 3.3 3.3l1.3-1 2.2 2-1.2 1.7C5.5 10.2 1.8 6.5 1 2.2z"/></svg>0207 555 0140</li>
        <li><svg viewBox="0 0 12 12"><path d="M3 0h6v12H3zM4 1.5v8h4v-8zM5.5 10.3h1v.9h-1z" fill-rule="evenodd"/></svg>07700 900 123</li>
        <li><svg viewBox="0 0 12 12"><path d="M3 0h6v3H3zM0 4h12v5h-2V7H2v2H0zM3 8h6v4H3z"/></svg>0207 555 0141</li>
        <li><svg viewBox="0 0 12 12"><path d="M0 2h12v1L6 7 0 3zM0 4.3l6 4 6-4V10H0z"/></svg>clerks@ledgerwoodchambers.com</li>
      </ul>
    </div>

    <p class="address">42 Temple Row, London<br>EC4Y 7AB</p>

    <div class="band-teal"></div>
    <div class="band-navy">www.ledgerwoodchambers.com</div>
  </section>
</body>
</html>
```